I need packaging artwork .with dielines, for scissors

“Brisa Edge”
Key elements to highlight on the packaging-
Ceramic Craft Scissors

Smoother than Titanium

Longer Lasting Blade Performance

Lighter, Easy to Use
Updates

Project Deadline Extended
Reason: Need more input on these concepts. Need softer, slightly more feminine font style- and must be open to expose the actual scissors.

Marlow Market(s)

Upper income consumer, with over $80,000 income. Typically shops a USA Marlow Store, Bulkora Store, Penwick Store, and a Craft retailer like Tallings and Ferrows

Font styles to use
Other font styles liked:
• BrisaEdge Aharoni

Requirements
Must have
• Bold swift design elements, in the World "BrisaEdge" as the product name.

Must emphase Ceramic blades for, easy, lighter, cleaner cuts- Must provide durability over even titanium scissors-
High endurance, consistently neat cuts, no fiber-squeezing or backlashing of fiber within the cutting angle zone of the shears – these are just a few of the many benefits of using zirconia cutting blade
Nice to have
• text on the back of the card with:

feature an ultra-sharp edge that lasts much longer than steel.
ultra sharp ceramic blades cut with precision and accuracy every time
scissors are made of an advanced, high-tech ceramic, second in hardness only to diamond,
These scissors are amazing. Pick a pair up and they are hard to put down.

ensure efficiency, effectiveness and will achieve more results, since the energy that is required when working with them is absolutely minimal.

a stronger and more resistant surface that protects against
wear and tear and increases cutting edge longevity.
Should not have
• too much text- bold, yet short concise messaging on the scissors benefits

```html
<!DOCTYPE html>
<html lang="en">
<head>
<meta charset="utf-8">
<title>BrisaEdge Ceramic Craft Scissors – Blister Card</title>
<link rel="stylesheet" href="https://fonts.googleapis.com/css2?family=Lato:ital,wght@0,400;0,700;0,900;1,700&family=Oswald:wght@300&family=Josefin+Sans:wght@400&display=swap">
<style>
  :root {
    --board-top: #3a2f96;
    --board-bottom: #2c2784;
    --card: #ffffff;
    --window: #dedede;
    --ink: #2b2b3a;
    --brand: #4a2f8a;
    --hole: #3b2d92;
    --label: #e6e2ff;
    --title: #cfc9ee;
    --pink: #e23a7a;
    --coral: #f07a5a;
    --peach: #f4b27f;
    --lilac: #c7a6e6;
    --icon: #ec4a6a;
  }
  * { margin: 0; padding: 0; box-sizing: border-box; }
  html, body { width: 1200px; height: 941px; overflow: hidden; }
  body {
    position: relative;
    background: linear-gradient(180deg, var(--board-top), var(--board-bottom));
    font-family: "Lato", sans-serif;
  }
  .board-title {
    position: absolute;
    left: 68px; top: 46px;
    font-family: "Lato", sans-serif;
    font-weight: 900;
    font-size: 84px;
    letter-spacing: -1px;
    color: var(--title);
  }
  .card-label {
    position: absolute;
    font-family: "Oswald", sans-serif;
    font-weight: 300;
    font-size: 18px;
    line-height: 21px;
    text-align: center;
    color: var(--label);
    letter-spacing: 0.5px;
  }
  .card-label--front { left: 170px; top: 716px; width: 130px; }
  .card-label--back { left: 405px; top: 240px; width: 130px; }
  .blister-card { position: absolute; display: block; }
  .blister-card--front { left: 140px; top: 196px; width: 181px; height: 497px; }
  .blister-card--back { left: 375px; top: 313px; width: 183px; height: 495px; }
  .brand-name { font-family: "Lato", sans-serif; font-weight: 900; fill: var(--brand); }
  .headline { font-family: "Josefin Sans", sans-serif; fill: var(--ink); }
  .benefit { font-family: "Lato", sans-serif; font-weight: 700; fill: var(--ink); }
  .feature-copy { font-family: "Lato", sans-serif; font-weight: 400; fill: var(--ink); }
  .tagline { font-family: "Lato", sans-serif; font-weight: 700; font-style: italic; fill: var(--ink); }
</style>
</head>
<body>
  <div class="board-title">BrisaEdge</div>

  <!-- Front of card -->
  <svg class="blister-card blister-card--front" viewBox="0 0 181 497" aria-label="Blister card front">
    <defs>
      <linearGradient id="ribbonWarm" x1="0" y1="0" x2="1" y2="1">
        <stop offset="0" stop-color="var(--pink)"/>
        <stop offset="0.5" stop-color="var(--coral)"/>
        <stop offset="1" stop-color="var(--peach)"/>
      </linearGradient>
      <linearGradient id="ribbonCool" x1="0" y1="0" x2="0" y2="1">
        <stop offset="0" stop-color="var(--pink)"/>
        <stop offset="1" stop-color="var(--lilac)"/>
      </linearGradient>
    </defs>
    <rect width="181" height="497" rx="12" fill="var(--card)"/>
    <rect x="72" y="9" width="37" height="15" rx="7.5" fill="var(--hole)"/>
    <path d="M0 6 C70 70 150 230 162 497 L175 497 C168 230 90 60 8 0 Z" fill="url(#ribbonCool)" opacity="0.55"/>
    <rect class="blister-window" x="20" y="58" width="141" height="410" rx="14" fill="var(--window)" role="img" aria-label="Clear blister window showing the ceramic craft scissors"/>
    <path d="M12 0 C90 60 168 200 181 340 L181 290 C160 180 100 60 40 0 Z" fill="url(#ribbonWarm)" opacity="0.7"/>
    <!-- label band -->
    <path d="M20 212 C70 190 130 196 176 228 L176 334 C120 318 60 302 20 300 Z" fill="var(--card)"/>
    <path d="M20 300 C60 302 120 318 176 334" fill="none" stroke="var(--pink)" stroke-width="2"/>
    <text class="brand-name" x="95" y="48" font-size="17" text-anchor="middle">BrisaEdge</text>
    <text class="headline" x="100" y="248" font-size="10.5" text-anchor="middle">CERAMIC</text>
    <text class="headline" x="100" y="258" font-size="7" text-anchor="middle">CRAFT SCISSORS</text>
    <line x1="72" y1="263" x2="128" y2="263" stroke="var(--ink)" stroke-width="0.6"/>
    <text class="benefit" x="100" y="273" font-size="5" text-anchor="middle">Smoother than Titanium</text>
    <text class="benefit" x="100" y="282" font-size="5" text-anchor="middle">Long-Lasting Blade Performance</text>
    <text class="benefit" x="100" y="291" font-size="5" text-anchor="middle">Light, Easy to Use</text>
    <text class="tagline" x="90.5" y="486" font-size="6.6" text-anchor="middle">Pick up a pair...and they'll be hard to put down!</text>
  </svg>

  <!-- Back of card -->
  <svg class="blister-card blister-card--back" viewBox="0 0 183 495" aria-label="Blister card back">
    <defs>
      <linearGradient id="bandSoft" x1="0" y1="0" x2="1" y2="0">
        <stop offset="0" stop-color="var(--peach)" stop-opacity="0.55"/>
        <stop offset="1" stop-color="var(--lilac)" stop-opacity="0.45"/>
      </linearGradient>
    </defs>
    <rect width="183" height="495" rx="12" fill="var(--card)"/>
    <rect x="73" y="9" width="37" height="15" rx="7.5" fill="var(--hole)"/>
    <path d="M0 40 C60 30 130 60 183 40 L183 52 C130 74 60 44 0 56 Z" fill="url(#bandSoft)"/>
    <path d="M0 110 C70 150 130 90 183 120 L183 135 C130 105 70 165 0 128 Z" fill="url(#bandSoft)"/>
    <path d="M60 175 C100 150 150 150 183 165 L183 178 C150 164 105 166 70 185 Z" fill="url(#bandSoft)"/>
    <path d="M0 370 C60 360 120 400 183 380 L183 392 C120 412 60 374 0 384 Z" fill="url(#bandSoft)"/>
    <path d="M0 448 C70 430 130 470 183 452 L183 468 C130 486 70 448 0 464 Z" fill="url(#bandSoft)"/>
    <text class="brand-name" x="91.5" y="44" font-size="17" text-anchor="middle">BrisaEdge</text>
    <text class="feature-copy" x="91.5" y="62" font-size="5.6" text-anchor="middle"><tspan font-weight="700">Minimum energy</tspan> required while working</text>
    <text class="headline" x="91.5" y="94" font-size="14" text-anchor="middle">Features:</text>

    <text class="feature-copy" x="91.5" y="116" font-size="4.4" text-anchor="middle">Ultra-sharp edge that lasts much longer than steel.</text>
    <rect x="73" y="138" width="37" height="26" rx="4" fill="var(--icon)" opacity="0.8" role="img" aria-label="Scissors icon"/>

    <text class="feature-copy" x="91.5" y="201" font-size="4.4" text-anchor="middle">Ceramic blades cut with precision and accuracy every time.</text>
    <g fill="none" stroke="var(--icon)" stroke-width="2" aria-label="Target icon">
      <circle cx="91.5" cy="240" r="16"/>
      <circle cx="91.5" cy="240" r="9"/>
      <circle cx="91.5" cy="240" r="3" fill="var(--icon)"/>
      <line x1="91.5" y1="240" x2="104" y2="227"/>
    </g>

    <text class="feature-copy" x="91.5" y="295" font-size="4.4" text-anchor="middle">Forged from a high-tech ceramic, second in hardness only to diamond.</text>
    <g aria-label="Diamond icon">
      <path d="M77 326 L84 318 L99 318 L106 326 L91.5 346 Z" fill="var(--icon)"/>
      <path d="M77 326 L106 326" stroke="#fff" stroke-width="1"/>
    </g>

    <text class="feature-copy" x="91.5" y="390" font-size="4.4" text-anchor="middle">Stronger and more resistant surface that protects against</text>
    <text class="feature-copy" x="91.5" y="397" font-size="4.4" text-anchor="middle">wear and tear and increases cutting edge longevity.</text>
    <rect x="72" y="418" width="39" height="34" rx="5" fill="var(--icon)" opacity="0.8" role="img" aria-label="Strength icon"/>
  </svg>

  <div class="card-label card-label--back">BLISTER CARD<br>(BACK)</div>
  <div class="card-label card-label--front">BLISTER CARD<br>(FRONT)</div>
</body>
</html>
```